Velvet Herb Company needs a label for a new line

We need a label design for a new product that is an off shoot of Cook Tobin's Grand Zestorama Seasonings. These new spice blends will be mixed into various condiments including but not limited to ketchup, mayonnaise and butter. We really like the new Brightleaf Pecan Pouch Sack. The label has to have the 1)Cook Tobin logo on it, 2) the the name of the product which is, "Blendettes" for ketchups, Blendettes for mayonnaise and Blendettes for Sour Cream, and then underneath that,3) the flavor i.e. Honeyed Curry Sriracha etc. The labels are going to be put on bags similar to the Brightleaf Pecan Pouch Sack. We actually also like their color combinations. We are going to need to have 3 different color combos because their will be 3 different condiments to mix the product into. There will also be 2 different size black bags that the spices will go in. The 2 oz. bag is 4" W x 2 3/8" G x 6 1/2" H and the 4 oz bag is 5 1/8" W x 3 1/8" G x 8 1/8" H. So we need 3 labels that will all be the same, just the color will need to be different and name of the condiment will change.

I have attached a file with our current spice label and a picture of the Brightleaf Pecan Sack that we like.
Updates

Hi Designer, Please note in the attached file there is a small image of our product with our current logo/image of Cook Tobin. Please use this (or use image on our site http://cooktobinsgrandzestorama.example/ ) as a placeholder for the logo until we find a better/higher-res file. We may also get our printer to swap the image when we go into print production. Thanks.

Target Market(s)

Home cooks and foodies. 25 - 45 year olds

Industry/Entity Type

It Company

Font styles to use
Sans Serif

Requirements
Must have
• Cook Tobin's picture and name

```html
<!DOCTYPE html>
<html lang="en">
<head>
<meta charset="utf-8">
<title>Cook Tobin's Blendettes – Condiment Labels</title>
<link rel="stylesheet" href="https://fonts.googleapis.com/css2?family=Montserrat:wght@700;800&family=Josefin+Sans:wght@300&family=Dancing+Script:wght@500&display=swap">
<style>
  :root {
    --stage: #000000;
    --ink: #0b0b0b;
    --paper: #ffffff;
    --paper-shade: #e6e6e6;
    --ketchup: #e41e26;
    --sour-cream: #15a9e8;
    --mayo: #9b1d62;
    --portrait-green: #6cb33f;
    --portrait-red: #c8262c;
  }
  * { box-sizing: border-box; margin: 0; padding: 0; }
  html, body {
    width: 1200px; height: 927px; overflow: hidden;
    background: var(--stage);
  }
  .sheet { position: relative; width: 1200px; height: 927px; }

  .label {
    position: absolute;
    width: 419px; height: 284px;
    border-radius: 14px;
    overflow: hidden;
    color: var(--ink);
    font-family: "Montserrat", sans-serif;
  }
  .label--ketchup    { left: 60px;  top: 95px;  --accent: var(--ketchup); }
  .label--sour-cream { left: 653px; top: 95px;  --accent: var(--sour-cream); }
  .label--mayo       { left: 397px; top: 499px; --accent: var(--mayo); }

  .label__shape { position: absolute; inset: 0; width: 100%; height: 100%; }
  .label__band { fill: var(--accent); }
  .label__panel { fill: url(#panelShade); }
  .label__edge { fill: none; stroke: var(--ink); stroke-width: 1.6; stroke-dasharray: 1.5 2.5; stroke-linecap: round; }

  .label__portrait {
    position: absolute; left: 9px; top: 11px;
    width: 52px; height: 52px; border-radius: 50%;
    border: 2px solid var(--paper);
    background: radial-gradient(circle at 50% 40%, #f3e6d8 0 28%, var(--portrait-red) 29% 52%, var(--portrait-green) 53%);
  }

  .label__brand {
    position: absolute; right: 8px; top: 27px;
    text-align: right; line-height: 1;
  }
  .brand__owner { display: block; font-size: 17px; font-weight: 700; letter-spacing: 0.2px; }
  .brand__name  { display: block; font-size: 39px; font-weight: 800; letter-spacing: -0.5px; margin-top: 1px; }
  .brand__for   { display: block; font-family: "Dancing Script", cursive; font-size: 12px; font-weight: 500; margin: -3px 22px 0 0; }
  .brand__condiment { display: block; font-size: 16px; font-weight: 700; margin-top: -4px; }

  .label__flavor {
    position: absolute; left: 0; right: 0; top: 152px;
    text-align: center; line-height: 1;
  }
  .flavor__lead {
    display: block; font-family: "Josefin Sans", sans-serif; font-weight: 300;
    font-size: 38px; letter-spacing: 0.5px; margin-right: 66px;
  }
  .flavor__name {
    display: block; font-size: 35px; font-weight: 800; letter-spacing: -0.6px;
    margin-top: 10px; padding-left: 16px;
  }

  .label__texture {
    position: absolute; left: 36px; top: 245px; width: 362px; height: 16px;
    background: linear-gradient(90deg, rgba(0,0,0,0.06), rgba(0,0,0,0.14), rgba(0,0,0,0.06));
    border-radius: 3px;
  }
</style>
</head>
<body>
<main class="sheet">
  <svg width="0" height="0" aria-hidden="true" style="position:absolute">
    <defs>
      <linearGradient id="panelShade" x1="0" y1="0" x2="1" y2="0">
        <stop offset="0" stop-color="#f7f7f7"/>
        <stop offset="0.5" stop-color="#ffffff"/>
        <stop offset="1" stop-color="#ececec"/>
      </linearGradient>
    </defs>
  </svg>

  <section class="label label--ketchup">
    <svg class="label__shape" viewBox="0 0 419 284" aria-hidden="true">
      <rect class="label__band" width="419" height="284"/>
      <path class="label__panel" d="M19 284 L19 210 C19 110 70 40 240 24 L419 10 L419 284 Z"/>
      <path class="label__edge" d="M19 284 L19 210 C19 110 70 40 240 24 L419 10"/>
    </svg>
    <div class="label__portrait" role="img" aria-label="Portrait of Cook Tobin"></div>
    <div class="label__brand">
      <span class="brand__owner">Cook Tobin's</span>
      <span class="brand__name">Blendettes</span>
      <span class="brand__for">for</span>
      <span class="brand__condiment">Ketchup</span>
    </div>
    <div class="label__flavor">
      <span class="flavor__lead">HONEYED</span>
      <span class="flavor__name">CURRY SRIRACHA</span>
    </div>
    <div class="label__texture" role="img" aria-label="Decorative speckle band"></div>
  </section>

  <section class="label label--sour-cream">
    <svg class="label__shape" viewBox="0 0 419 284" aria-hidden="true">
      <rect class="label__band" width="419" height="284"/>
      <path class="label__panel" d="M19 284 L19 210 C19 110 70 40 240 24 L419 10 L419 284 Z"/>
      <path class="label__edge" d="M19 284 L19 210 C19 110 70 40 240 24 L419 10"/>
    </svg>
    <div class="label__portrait" role="img" aria-label="Portrait of Cook Tobin"></div>
    <div class="label__brand">
      <span class="brand__owner">Cook Tobin's</span>
      <span class="brand__name">Blendettes</span>
      <span class="brand__for">for</span>
      <span class="brand__condiment">Sour Cream</span>
    </div>
    <div class="label__flavor">
      <span class="flavor__lead">HONEYED</span>
      <span class="flavor__name">CURRY SRIRACHA</span>
    </div>
    <div class="label__texture" role="img" aria-label="Decorative speckle band"></div>
  </section>

  <section class="label label--mayo">
    <svg class="label__shape" viewBox="0 0 419 284" aria-hidden="true">
      <rect class="label__band" width="419" height="284"/>
      <path class="label__panel" d="M19 284 L19 210 C19 110 70 40 240 24 L419 10 L419 284 Z"/>
      <path class="label__edge" d="M19 284 L19 210 C19 110 70 40 240 24 L419 10"/>
    </svg>
    <div class="label__portrait" role="img" aria-label="Portrait of Cook Tobin"></div>
    <div class="label__brand">
      <span class="brand__owner">Cook Tobin's</span>
      <span class="brand__name">Blendettes</span>
      <span class="brand__for">for</span>
      <span class="brand__condiment">Mayo</span>
    </div>
    <div class="label__flavor">
      <span class="flavor__lead">HONEYED</span>
      <span class="flavor__name">CURRY SRIRACHA</span>
    </div>
    <div class="label__texture" role="img" aria-label="Decorative speckle band"></div>
  </section>
</main>
</body>
</html>
```